Chicken Wing A0 and A4 Poster

Our restaurant name is Tavlo Grill

We have introduced chicken wings to our menu. They are deep fried and mixed with different sauce selections.

The sauce options are: Tavlo BBQ, Regular BBQ, Sweet Chili and Garlic, Hot Chili, Garlic

Available in a 6, 10 or 20 Pack.
Larger Catering Packs Available

We have uploaded some pictures from the internet with chicken wings.

We also have 4 other poster designs coming in the next 3 weeks.

Restaurant

```html
<!DOCTYPE html>
<html lang="en">
<head>
<meta charset="utf-8">
<title>Tavlo Grill – Chicken Wings Poster</title>
<link rel="stylesheet" href="https://fonts.googleapis.com/css2?family=Baloo+2:wght@500;700;800&family=Chewy&family=Oswald:wght@500;700&family=Montserrat:wght@700&family=Arimo:wght@400;700&display=swap">
<style>
  :root {
    --stage: #262626;
    --olive: #7e7a17;
    --lime: #b7c030;
    --yellow: #f3e33a;
    --gold: #f6c915;
    --orange: #f8a81a;
    --crimson: #a8103c;
    --salmon: #d9836b;
    --purple: #6b0f5a;
    --ink: #111111;
    --white: #ffffff;
  }
  * { box-sizing: border-box; margin: 0; padding: 0; }
  html, body { width: 928px; height: 1200px; overflow: hidden; }
  body { background: var(--stage); position: relative; }

  .flyer {
    position: absolute; left: 44px; top: 7px;
    width: 840px; height: 1186px;
    background: var(--crimson);
    overflow: hidden;
    font-family: "Baloo 2", sans-serif;
  }
  .photo-main {
    position: absolute; left: 225px; top: 120px; width: 615px; height: 600px;
    background: radial-gradient(ellipse at 40% 45%, #c8521c 0%, #e07a2c 35%, #f0a868 65%, #f6d2b0 100%);
  }
  .photo-side {
    position: absolute; left: 0; top: 0; width: 225px; height: 700px;
    background: linear-gradient(180deg, #f2d2a6 0%, #e9b47a 40%, #cfa061 70%, #d7b98a 100%);
    opacity: .9;
  }
  .photo-top {
    position: absolute; left: 225px; top: 0; width: 615px; height: 120px;
    background: linear-gradient(90deg, #f2c79a, #f3b88a 60%, #eaa57a);
  }
  .shapes { position: absolute; left: 0; top: 0; width: 840px; height: 1186px; }

  .header-bar {
    position: absolute; left: 0; top: 54px; width: 840px; height: 12px; background: var(--olive);
  }
  .phone-band {
    position: absolute; right: 0; top: 66px; width: 424px; height: 74px;
    background: var(--ink); border-bottom: 12px solid var(--olive);
    display: flex; align-items: center; justify-content: flex-end; gap: 14px; padding-right: 28px;
    color: var(--white); font-family: "Oswald", sans-serif; font-weight: 500; font-size: 38px;
  }
  .phone-band svg { width: 30px; height: 30px; }

  .brand {
    position: absolute; left: 108px; top: -56px; width: 278px; height: 278px;
    border-radius: 50%; background: var(--olive);
    border: 6px solid #3b3a10;
    display: flex; flex-direction: column; align-items: center; justify-content: center;
    padding-top: 60px;
  }
  .brand-name {
    font-family: "Baloo 2", sans-serif; font-weight: 800; font-size: 50px; line-height: 1;
    color: var(--white); white-space: nowrap;
  }
  .brand-tag {
    font-family: "Baloo 2", sans-serif; font-weight: 700; font-size: 14px; letter-spacing: 2px;
    color: var(--white); text-transform: uppercase; margin-top: 4px;
  }

  .special {
    position: absolute; left: 558px; top: 381px; width: 272px; height: 272px;
  }
  .special-text {
    position: absolute; inset: 0; display: flex; flex-direction: column; align-items: center; justify-content: center;
    font-family: "Oswald", sans-serif; color: var(--yellow); padding-top: 6px;
  }
  .special-price { font-weight: 700; font-size: 100px; line-height: .95; display: flex; align-items: flex-start; }
  .special-price sup { font-size: 34px; line-height: 1; margin-top: 14px; }
  .special-label {
    font-family: "Montserrat", sans-serif; font-weight: 700; font-size: 18px; line-height: 1.05;
    color: var(--white); text-align: center; margin-top: 4px;
  }

  .dish { position: absolute; left: 26px; width: 270px; height: 270px; }
  .dish-photo {
    position: absolute; left: 8px; top: 0; width: 254px; height: 254px; border-radius: 50%;
    border: 9px solid var(--purple); box-shadow: 0 0 0 3px var(--white) inset;
  }
  .dish-wings .dish-photo { background: radial-gradient(circle at 50% 45%, #e48a3a 0%, #c95a1e 35%, #9c3c14 60%, #e8d3b8 85%); }
  .dish-platter .dish-photo { background: radial-gradient(circle at 55% 50%, #d78a3c 0%, #b65a22 30%, #c9a44a 55%, #e6c879 75%, #f1ede2 92%); }
  .dish-count {
    position: absolute; left: 196px; top: -30px; width: 96px; height: 96px; border-radius: 50%;
    background: var(--olive); border: 5px solid var(--white);
    display: flex; align-items: center; justify-content: center;
    color: var(--white); font-family: "Oswald", sans-serif; font-weight: 500; font-size: 46px;
  }
  .dish-label {
    position: absolute; left: 37px; top: 190px; width: 198px; height: 54px;
    border-radius: 12px; background: var(--olive); border: 3px solid var(--white);
    display: flex; align-items: center; justify-content: center;
    color: var(--white); font-family: "Baloo 2", sans-serif; font-weight: 500; font-size: 28px;
  }
  .dish-wings { top: 568px; }
  .dish-platter { top: 850px; }

  .headline {
    position: absolute; right: 38px; top: 712px; text-align: right; color: var(--white);
  }
  .headline-top { font-family: "Baloo 2", sans-serif; font-weight: 500; font-size: 48px; line-height: 1; }
  .headline-item {
    font-family: "Chewy", "Baloo 2", sans-serif; font-size: 56px; line-height: 1; color: var(--orange);
    margin: 4px 30px 0 0;
  }
  .headline-bottom { font-family: "Baloo 2", sans-serif; font-weight: 500; font-size: 37px; line-height: 1.1; }

  .details {
    position: absolute; left: 340px; top: 966px; list-style: none;
    font-family: "Arimo", sans-serif; font-size: 20px; line-height: 26px; color: var(--gold);
  }
  .details strong { font-weight: 700; }

  .footer {
    position: absolute; left: 0; top: 1132px; width: 840px; height: 54px; background: var(--purple);
    display: flex; align-items: center; justify-content: space-between; padding: 0 40px 4px 62px;
    color: var(--white); font-family: "Montserrat", sans-serif; font-weight: 700; font-size: 22px;
  }
  .footer-delivery span { margin-left: 22px; }
</style>
</head>
<body>
  <main class="flyer">
    <div class="photo-side" role="img" aria-label="Photo of sauced chicken wings with fresh herbs"></div>
    <div class="photo-top" role="img" aria-label="Blurred background photo of fried chicken wings"></div>
    <div class="photo-main" role="img" aria-label="Photo of glazed barbecue chicken wings on a plate"></div>

    <svg class="shapes" viewBox="0 0 840 1186" aria-hidden="true">
      <path d="M0 700 Q 330 610 840 560 L840 1132 L0 1132 Z" fill="var(--crimson)"/>
      <rect x="0" y="700" width="225" height="432" fill="var(--salmon)"/>
      <path d="M0 662 Q 300 600 560 590 Q 700 585 840 548 L840 566 Q 620 620 420 660 Q 200 690 0 720 Z" fill="var(--ink)"/>
      <path d="M0 640 Q 300 580 560 575 Q 700 570 840 532 L840 552 Q 620 604 420 640 Q 200 672 0 700 Z" fill="var(--lime)"/>
    </svg>

    <div class="header-bar"></div>
    <div class="phone-band">
      <svg viewBox="0 0 24 24" aria-hidden="true"><path fill="#f6c915" d="M6.6 10.8a15 15 0 0 0 6.6 6.6l2.2-2.2c.3-.3.7-.4 1-.2 1.1.4 2.3.6 3.6.6.6 0 1 .4 1 1V20c0 .6-.4 1-1 1A17 17 0 0 1 3 4c0-.6.4-1 1-1h3.5c.6 0 1 .4 1 1 0 1.3.2 2.5.6 3.6.1.3 0 .7-.2 1Z"/></svg>
      <span>555-0142-880</span>
    </div>

    <div class="brand">
      <div class="brand-name">Tavlo Grill</div>
      <div class="brand-tag">Authentic Lebanese Food</div>
    </div>

    <div class="special">
      <svg viewBox="0 0 272 272" width="272" height="272" aria-hidden="true">
        <defs>
          <g id="petals">
            <circle cx="96" cy="0" r="40"/><circle cx="77.7" cy="56.4" r="40"/><circle cx="29.7" cy="91.3" r="40"/>
            <circle cx="-29.7" cy="91.3" r="40"/><circle cx="-77.7" cy="56.4" r="40"/><circle cx="-96" cy="0" r="40"/>
            <circle cx="-77.7" cy="-56.4" r="40"/><circle cx="-29.7" cy="-91.3" r="40"/><circle cx="29.7" cy="-91.3" r="40"/>
            <circle cx="77.7" cy="-56.4" r="40"/><circle cx="0" cy="0" r="100"/>
          </g>
        </defs>
        <g transform="translate(136 136)">
          <use href="#petals" fill="#f3e33a"/>
          <use href="#petals" fill="#7e7a17" transform="scale(.9)"/>
        </g>
      </svg>
      <div class="special-text">
        <div class="special-price">$4<sup>.99</sup></div>
        <div class="special-label">6 PACK<br>SPECIAL</div>
      </div>
    </div>

    <div class="dish dish-wings">
      <div class="dish-photo" role="img" aria-label="Photo of a basket of saucy chicken wings"></div>
      <div class="dish-count">10</div>
      <div class="dish-label">10 Pack</div>
    </div>
    <div class="dish dish-platter">
      <div class="dish-photo" role="img" aria-label="Photo of a large platter of chicken wings"></div>
      <div class="dish-count">20</div>
      <div class="dish-label">20 Pack</div>
    </div>

    <div class="headline">
      <div class="headline-top">Delicious</div>
      <div class="headline-item">Chicken Wings</div>
      <div class="headline-bottom">that won’t hurt your wallet</div>
    </div>

    <ul class="details">
      <li><strong>Sauces:</strong> Tavlo BBQ, Regular BBQ, Sweet Chili</li>
      <li>and Garlic, Hot Chili, Garlic</li>
      <li>Available in a 6, 10 or 20 Pack</li>
      <li>Larger Catering Packs Available</li>
      <li>Phone: +63 5550142880</li>
    </ul>

    <footer class="footer">
      <div class="footer-delivery">DELIVERY SERVICE: <span>555-0142 880</span></div>
      <div class="footer-web">WWW.TAVLOGRILL.COM</div>
    </footer>
  </main>
</body>
</html>
```